need label redone so i can edit it, it was ai generated.

Hey, this label design was originally generated by AI, and while I like the overall layout, there are several issues with it. Some elements are not lossless, others appear distorted, uneditable, or low quality.
What I need is a complete recreation of this label—exactly as it is—without adding any new creative touches. Please rebuild every element of the label from scratch, but make sure the final file is in a fully editable, high-resolution format (preferably an .ai file or equivalent).
Each part of the label (text, shapes, background, colors, etc.) should be separated into layers or components so I can easily change anything I want later—like the font, colors, text, or images.
Quality and editability are the top priorities here. Please make sure the design is 100% lossless and flexible for editing.

```html
<!DOCTYPE html>
<html lang="en">
<head>
<meta charset="utf-8">
<title>TIDETAIL Dog Beach Towel Label</title>
<link href="https://fonts.googleapis.com/css2?family=Fredoka:wght@600;700&family=Barlow+Condensed:wght@600;700&family=Sansita:ital,wght@1,800&display=swap" rel="stylesheet">
<style>
  :root {
    --page: #ffffff;
    --sky: #93d4d8;
    --sky-band: #80cad2;
    --navy: #054a6c;
    --orange: #e68a26;
    --cream: #f2e4cf;
    --yellow: #ffd200;
    --sand-light: #f3d8a2;
    --sand: #e4c287;
  }
  * { margin: 0; padding: 0; box-sizing: border-box; }
  html, body { width: 902px; height: 1200px; overflow: hidden; background: var(--page); }
  .canvas { position: relative; width: 902px; height: 1200px; }
  .label {
    position: absolute; left: 67px; top: 91px; width: 759px; height: 1010px;
    background: var(--sky); overflow: hidden;
    font-family: "Fredoka", sans-serif;
  }
  .label-shapes { position: absolute; inset: 0; }
  .brand {
    position: absolute; left: 155px; top: 52px;
    display: flex; align-items: center; gap: 12px;
  }
  .brand-dot { width: 54px; height: 54px; border-radius: 50%; background: var(--navy); flex: none; }
  .brand-name {
    font-family: "Fredoka", sans-serif; font-weight: 700; font-size: 74px;
    line-height: 1; color: var(--navy); letter-spacing: 1px; white-space: nowrap;
  }
  .kicker {
    position: absolute; left: 90px; top: 172px; width: 250px; height: 111px;
    transform: rotate(-5deg);
    background: var(--orange); border-radius: 50%;
    display: flex; flex-direction: column; align-items: center; justify-content: center;
    font-family: "Barlow Condensed", sans-serif; font-weight: 700; color: var(--cream);
    font-size: 29px; line-height: 1; text-align: center; white-space: nowrap;
  }
  .headline { font-family: "Fredoka", sans-serif; font-weight: 700; color: var(--cream); }
  .headline-line {
    position: absolute; display: block; line-height: 1; white-space: nowrap;
    letter-spacing: -1px; transform: rotate(-6.2deg); transform-origin: 0 85%;
  }
  .headline .line-1 { left: 103px; top: 303px; font-size: 82px; }
  .headline .line-2 { left: 129px; top: 378px; font-size: 92px; }
  .tagline {
    position: absolute; left: 98px; top: 480px;
    transform: rotate(-6.8deg); transform-origin: 0 85%;
    font-family: "Sansita", sans-serif; font-style: italic; font-weight: 800;
    font-size: 36px; line-height: 1; color: var(--yellow); white-space: nowrap;
  }
  .badge {
    position: absolute; border-radius: 50%;
    display: flex; flex-direction: column; align-items: center; justify-content: center;
    text-align: center; font-family: "Barlow Condensed", sans-serif; font-weight: 700;
    color: var(--cream); line-height: 0.95; white-space: nowrap;
  }
  .badge-absorbent { left: 75px; top: 571px; width: 141px; height: 151px; background: var(--orange); }
  .badge-absorbent .big { font-family: "Fredoka", sans-serif; font-size: 66px; line-height: 0.9; }
  .badge-absorbent .small { font-size: 25px; }
  .badge-car { left: 75px; top: 738px; width: 134px; height: 145px; background: var(--navy); font-size: 29px; }
  .badge-bag { left: 210px; top: 681px; width: 132px; height: 145px; background: var(--navy); font-size: 29px; }
  .badge-bag .small { font-size: 21px; margin-top: 3px; }
  .closing {
    position: absolute; left: 20px; top: 906px;
    font-family: "Barlow Condensed", sans-serif; font-weight: 700; font-size: 34px;
    line-height: 1.18; color: var(--navy); white-space: nowrap;
  }
  .features {
    position: absolute; left: 563px; top: 943px; display: flex; gap: 9px; list-style: none;
  }
  .feature { width: 30px; display: flex; flex-direction: column; align-items: center; }
  .feature-icon { width: 26px; height: 26px; }
  .feature-text {
    margin-top: 3px; font-family: "Barlow Condensed", sans-serif; font-weight: 600;
    font-size: 7.5px; line-height: 1.05; color: var(--navy); text-align: center; white-space: nowrap;
  }
</style>
</head>
<body>
<div class="canvas">
  <section class="label">
    <svg class="label-shapes" viewBox="0 0 759 1010" width="759" height="1010" aria-hidden="true">
      <defs>
        <linearGradient id="scene-tone" x1="0" y1="0" x2="0" y2="1">
          <stop offset="0" stop-color="#5fc4cb"/>
          <stop offset="0.32" stop-color="#1e8f98"/>
          <stop offset="0.52" stop-color="#e8c78d"/>
          <stop offset="0.75" stop-color="#c98a3c"/>
          <stop offset="1" stop-color="#e2b872"/>
        </linearGradient>
      </defs>
      <path class="sky-band" d="M0,200 C80,205 160,160 260,145 C340,135 420,165 500,150 C600,135 680,150 759,185 V760 H0 Z" fill="var(--sky-band)"/>
      <path class="sky-band-low" d="M0,620 C60,605 120,600 180,612 C300,640 400,600 500,560 C600,525 690,540 759,570 V760 H0 Z" fill="#7ec8cf"/>
      <path class="sand-left" d="M0,715 C80,735 150,742 230,740 L260,900 H0 Z" fill="var(--sand-light)"/>
      <path class="scene" role="img" aria-label="Beach scene with sea, sand and a golden retriever wrapped in a teal towel" d="M210,613 H690 V860 C690,945 645,972 560,972 C430,972 330,940 220,880 C170,853 120,838 60,830 L0,826 V742 C80,752 150,745 210,735 Z" fill="url(#scene-tone)"/>
      <path class="sand-band" d="M0,885 C150,880 260,905 380,950 C450,975 520,976 570,974 C640,971 690,950 759,940 V1010 H0 Z" fill="var(--sand)"/>
      <path class="banner" d="M60,305 C60,255 90,240 140,236 L560,183 C650,176 697,210 697,270 L690,527 C560,495 420,510 300,535 C230,550 180,556 150,554 C95,552 60,520 60,470 Z" fill="var(--navy)"/>
    </svg>

    <div class="brand">
      <span class="brand-dot"></span>
      <span class="brand-name">TIDETAIL</span>
    </div>

    <div class="kicker"><span>DRY YOUR DOG</span><span>FASTER THAN EVER!</span></div>

    <h1 class="headline">
      <span class="headline-line line-1">DRY YOUR DOG</span>
      <span class="headline-line line-2">IN SECONDS</span>
    </h1>
    <p class="tagline">The Ultimate Beach Towel for Dogs</p>

    <div class="badge badge-absorbent"><span class="big">5x</span><span class="small">MORE</span><span class="small">ABSORBENT</span></div>
    <div class="badge badge-bag"><span>BEACH</span><span>BAG</span><span class="small">MUST-HAVE</span></div>
    <div class="badge badge-car"><span>NO MORE</span><span>WET CAR</span><span>RIDES</span></div>

    <p class="closing">Trade the Stack of<br>towels for One That Works.</p>

    <ul class="features">
      <li class="feature">
        <svg class="feature-icon" viewBox="0 0 26 26"><circle cx="13" cy="13" r="11.5" fill="none" stroke="var(--navy)" stroke-width="1.5"/><rect x="7.5" y="7" width="11" height="12" rx="1.5" fill="none" stroke="var(--navy)" stroke-width="1.4"/><circle cx="13" cy="14" r="3" fill="var(--navy)"/></svg>
        <span class="feature-text">MACHINE<br>WASHABLE</span>
      </li>
      <li class="feature">
        <svg class="feature-icon" viewBox="0 0 26 26"><circle cx="13" cy="13" r="11.5" fill="none" stroke="var(--navy)" stroke-width="1.5"/><path d="M12,6 C9,11 8,13 8,15 A4,4 0 0 0 16,15 C16,13 15,11 12,6 Z" fill="var(--navy)"/><circle cx="17" cy="17" r="3" fill="#fff" stroke="var(--navy)" stroke-width="1"/></svg>
        <span class="feature-text">FAST<br>DRYING</span>
      </li>
      <li class="feature">
        <svg class="feature-icon" viewBox="0 0 26 26"><circle cx="13" cy="13" r="11.5" fill="none" stroke="var(--navy)" stroke-width="1.5"/><path d="M13,6 C8,10 8,16 13,19 C18,16 18,10 13,6 Z M13,8 V21" fill="none" stroke="var(--navy)" stroke-width="1.4"/></svg>
        <span class="feature-text">ECO<br>FRIENDLY</span>
      </li>
    </ul>
  </section>
</div>
</body>
</html>
```